Global Outreach Fellowship needs a Book Cover Design Project

I am a pastor, missionary, author, and the founder of a non-profit organization. I am in the process of publishing a book focused on "The Spirit of a Faithful Shepherd" and desire a contemporary, even somewhat abstract book cover. Here is a link to the company's web page portfolio that designed our Web Page, to give you an idea of the style of cover that I am looking for. http://www.pixelharborstudio.com/cd-covers

Though the book is obviously targeted toward Christians, I want it to be attractive enough to capture the attention of the general population as well.

Industry/Entity Type

Non-Profit

```html
<!DOCTYPE html>
<html lang="en">
<head>
<meta charset="utf-8">
<title>The Spirit of a Faithful Shepherd – Book Cover</title>
<link rel="stylesheet" href="https://fonts.googleapis.com/css2?family=Belleza&display=swap">
<style>
  :root {
    --page: #ffffff;
    --ink-dark: #161616;
    --cover-black: #070707;
    --smoke-dark: #3c3c3c;
    --smoke: #7a7a7a;
    --mist: #c4c4c4;
    --sky-bright: #f4f4f4;
    --stone-pale: #f0dcae;
    --stone-light: #d9b77c;
    --stone-warm: #a87a3e;
    --stone-deep: #4a3520;
    --gold: #a88a12;
    --text-light: #ffffff;
    --placeholder: #ffffff;
  }
  * { margin: 0; padding: 0; box-sizing: border-box; }
  html, body {
    width: 1200px;
    height: 949px;
    overflow: hidden;
    background: var(--page);
  }
  .canvas {
    position: relative;
    width: 1200px;
    height: 949px;
    background: var(--page);
  }
  .cover-spread {
    position: absolute;
    left: 64px;
    top: 58px;
    width: 1084px;
    height: 814px;
    overflow: hidden;
    background: var(--cover-black);
    box-shadow: 6px 8px 10px rgba(0, 0, 0, 0.35);
  }
  .cover-art {
    position: absolute;
    inset: 0;
    background:
      /* front: sky behind title */
      radial-gradient(ellipse 360px 150px at 820px 90px, var(--sky-bright) 0%, var(--mist) 38%, var(--smoke) 68%, rgba(30,30,30,0) 100%),
      radial-gradient(ellipse 300px 90px at 760px 260px, rgba(150,150,150,0.7) 0%, rgba(40,40,40,0) 100%),
      /* front: stone wing */
      radial-gradient(ellipse 210px 300px at 900px 560px, var(--stone-pale) 0%, var(--stone-light) 35%, var(--stone-warm) 65%, rgba(60,40,20,0) 100%),
      radial-gradient(ellipse 110px 260px at 980px 620px, rgba(240,220,174,0.9) 0%, rgba(120,90,50,0) 100%),
      /* front: dim arm near spine */
      radial-gradient(ellipse 70px 320px at 610px 560px, rgba(120,80,40,0.8) 0%, rgba(40,25,12,0) 100%),
      radial-gradient(ellipse 90px 160px at 650px 210px, rgba(110,110,110,0.6) 0%, rgba(30,30,30,0) 100%),
      /* back: stone shoulder */
      radial-gradient(ellipse 330px 170px at 280px 700px, var(--stone-pale) 0%, var(--stone-light) 30%, var(--stone-warm) 60%, rgba(60,40,20,0) 100%),
      radial-gradient(ellipse 200px 110px at 440px 760px, rgba(170,120,60,0.8) 0%, rgba(60,40,20,0) 100%),
      /* back: smoke and shadowed figure */
      radial-gradient(ellipse 180px 160px at 270px 400px, var(--smoke-dark) 0%, rgba(20,20,20,0) 100%),
      radial-gradient(ellipse 140px 120px at 60px 360px, rgba(110,110,110,0.7) 0%, rgba(30,30,30,0) 100%),
      radial-gradient(ellipse 480px 150px at 220px 40px, var(--smoke) 0%, rgba(40,40,40,0.6) 50%, rgba(20,20,20,0) 100%),
      var(--cover-black);
  }
  .spine {
    position: absolute;
    left: 522px;
    top: 0;
    width: 42px;
    height: 814px;
    background: var(--gold);
  }
  .spine-title {
    position: absolute;
    left: 50%;
    top: 58px;
    transform-origin: left top;
    transform: translateX(14px) rotate(90deg);
    white-space: nowrap;
    font-family: "Belleza", sans-serif;
    font-weight: 400;
    font-size: 24px;
    color: var(--text-light);
  }
  .back-title {
    position: absolute;
    left: 46px;
    top: 64px;
    font-family: "Belleza", sans-serif;
    font-weight: 400;
    font-size: 24px;
    color: var(--text-light);
  }
  .back-rule {
    position: absolute;
    left: 46px;
    top: 98px;
    width: 394px;
    height: 2px;
    background: var(--gold);
  }
  .back-blurb {
    position: absolute;
    left: 46px;
    top: 110px;
    width: 390px;
    font-family: "Belleza", sans-serif;
    font-size: 15.5px;
    line-height: 20px;
    color: var(--text-light);
  }
  .barcode-area {
    position: absolute;
    left: 48px;
    top: 685px;
    width: 172px;
    height: 93px;
    background: var(--placeholder);
  }
  .front-title {
    position: absolute;
    right: 68px;
    top: 64px;
    text-align: right;
    font-family: "Belleza", sans-serif;
    font-weight: 400;
    color: var(--ink-dark);
  }
  .front-title-main {
    display: block;
    font-size: 62px;
    line-height: 66px;
  }
  .front-rule {
    display: block;
    height: 2px;
    margin: 0 0 4px 10px;
    background: var(--gold);
  }
  .front-title-sub {
    display: block;
    font-size: 26px;
    line-height: 30px;
  }
  .author-name {
    position: absolute;
    left: 694px;
    top: 752px;
    font-family: "Belleza", sans-serif;
    font-size: 24px;
    letter-spacing: 3.5px;
    color: var(--text-light);
  }
</style>
</head>
<body>
<div class="canvas">
  <section class="cover-spread">
    <div class="cover-art" role="img" aria-label="Dramatic photograph of a weathered stone angel statue under a cloudy grey sky, warm light on the folded wing and shoulder"></div>

    <div class="back-cover">
      <h2 class="back-title">The Spirit of a Faithful Shepherd</h2>
      <div class="back-rule"></div>
      <p class="back-blurb">Lorem ipsum dolor sit amet, consectetur adipisicing elit, sed do eiusmod tempor incididunt ut labore et dolore magna aliqua. Ut enim ad minim veniam, quis nostrud exercitation ullamco laboris nisi ut aliquip ex ea commodo consequat. Duis aute irure dolor in reprehenderit in voluptate velit esse cillum dolore eu fugiat nulla pariatur. Excepteur sint occaecat cupidatat non proident, sunt in culpa qui officia deserunt mollit anim id est laborum.</p>
      <div class="barcode-area"></div>
    </div>

    <div class="spine">
      <span class="spine-title">The Spirit of a Faithful Shepherd</span>
    </div>

    <div class="front-cover">
      <h1 class="front-title">
        <span class="front-title-main">The Spirit</span>
        <span class="front-rule"></span>
        <span class="front-title-sub">of a Faithful Shepherd</span>
      </h1>
      <p class="author-name">Authors name here</p>
    </div>
  </section>
</div>
</body>
</html>
```